Home Care App Design

We would like a responsive app design (mobile/web) for an app that will be used by our staff. These need to work display nearly the same for iPhone and Android. The app tracks caregiver tasks (check-in time, daily client activities, caregiver notes, and check out time) and provides updates to team and family members
Updates

I have added individual or grouped pages with better resolution. please let me know if you have any questions

we did not get enough entries so we increase the budget and have not received any new designer entries

Target Market(s)

professional caregivers and family members

Industry/Entity Type

Home Health Care

Font styles to use
Serif

Requirements
Must have
• We currently have a logo - please use colors or slight variants
• We also will need pop-up designs for informational messages and call to actions (with 1-3 options)
Nice to have
• I have attached a sketch of the app, please use this as a guideline. We are looking for ease of use.
• Please feel free to add design aspects that will make it easy to navigate, select options, or enter notes/messages

```html
<!DOCTYPE html>
<html lang="en">
<head>
<meta charset="utf-8">
<title>Home Care App – Messages &amp; Team Carer</title>
<link rel="stylesheet" href="https://fonts.googleapis.com/css2?family=Alegreya:wght@400;500&family=Roboto+Slab:wght@300;400&display=swap">
<style>
  :root{
    --backdrop:#e8e8e8;
    --screen:#ffffff;
    --brand:#3d5afe;
    --brand-soft:#7b8cf5;
    --ink:#2b2b33;
    --ink-muted:#7a7a82;
    --rule:#dcdcdc;
    --card:#f4f5fa;
    --star:#f2c230;
    --star-off:#c9c9cf;
    --avatar-warm:#8a6a5a;
    --avatar-light:#d9b98e;
  }
  *{box-sizing:border-box;margin:0;padding:0}
  html,body{width:1200px;height:1000px;overflow:hidden}
  body{background:var(--backdrop);font-family:"Alegreya",Georgia,serif;color:var(--ink);position:relative}
  .screen{position:absolute;width:400px;height:866px;background:var(--screen);overflow:hidden}
  .screen--messages{left:150px;top:69px}
  .screen--team{left:649px;top:67px}
  .status-bar{position:absolute;left:0;top:0;width:100%;height:46px}
  .status-time{position:absolute;left:38px;top:18px;font:500 15px "Roboto Slab",serif}
  .status-icons{position:absolute;right:20px;top:18px}
  .app-header{position:absolute;left:0;top:46px;width:100%;height:64px;background:var(--brand);color:#fff;
    display:flex;align-items:center;justify-content:center;font-size:27px;font-weight:500}
  .abs{position:absolute}
  /* Messages */
  .pending{right:33px;top:142px;font-size:15px;color:var(--ink-muted)}
  .task{position:absolute;left:34px;width:332px}
  .task-icon{position:absolute;left:0;top:0}
  .task-text{position:absolute;left:34px;top:0;font-size:16px;line-height:26px}
  .task-date{position:absolute;right:-2px;font:300 11px "Roboto Slab",serif;color:var(--ink)}
  .task-rule{position:absolute;left:0;width:332px;height:2px;background:var(--rule)}
  .notification{left:256px;top:477px;width:128px;height:170px;border:1px solid var(--brand-soft);border-radius:3px;
    background:#fff;box-shadow:3px 3px 0 rgba(61,90,254,.35);font-size:14px;text-align:center;padding-top:14px}
  .tool{position:absolute;top:660px;width:110px;text-align:center;font-size:17px;color:#444}
  .tool svg{display:block;margin:0 auto 8px}
  .tab-bar{position:absolute;left:0;bottom:0;width:100%;height:94px;background:#fff;border-radius:16px 16px 0 0;
    box-shadow:0 -20px 30px rgba(0,0,0,.035)}
  .tab{position:absolute;top:14px;width:60px;text-align:center;font:400 8px "Roboto Slab",serif;color:#222}
  .tab svg{display:block;margin:0 auto 3px}
  .tab--active{color:var(--brand)}
  /* Team */
  .sort-label{left:205px;top:141px;font-size:14px;color:#444}
  .sort-select{left:256px;top:137px;width:128px;height:25px;border:1px solid var(--brand)}
  .sort-select svg{position:absolute;right:8px;top:6px}
  .carer-card{position:absolute;left:17px;width:367px;height:102px;background:var(--card);border-radius:12px}
  .avatar{position:absolute;left:17px;top:17px;width:68px;height:68px;border-radius:50%;border:1px solid var(--brand)}
  .carer-name{position:absolute;left:102px;top:34px;font-size:16px}
  .carer-role{position:absolute;left:102px;top:59px;font-size:14px;color:var(--ink-muted)}
  .carer-phone{position:absolute;left:246px;top:42px;font:300 13px "Roboto Slab",serif;color:#444;display:flex;align-items:center;gap:8px}
  .divider{left:17px;top:434px;width:367px;height:2px;background:var(--rule)}
  .stat-label{position:absolute;font-size:11px;color:var(--ink)}
  .stat-value{position:absolute;right:17px;font-size:16px;font-weight:500;color:var(--brand-soft)}
  .stars{position:absolute;left:88px}
  .chart{left:0;top:0}
  .axis-label{font:400 13px "Roboto Slab",serif;fill:var(--ink)}
</style>
</head>
<body>
<svg width="0" height="0" style="position:absolute">
  <defs>
    <symbol id="star" viewBox="0 0 12 12"><path d="M6 .8l1.5 3.3 3.6.4-2.7 2.4.8 3.6L6 8.7 2.8 10.5l.8-3.6L.9 4.5l3.6-.4z"/></symbol>
    <symbol id="signal" viewBox="0 0 58 12">
      <rect x="0" y="8" width="3" height="4" rx="1" fill="#111"/><rect x="4.5" y="6" width="3" height="6" rx="1" fill="#111"/>
      <rect x="9" y="3.5" width="3" height="8.5" rx="1" fill="#111"/><rect x="13.5" y="1" width="3" height="11" rx="1" fill="#111"/>
      <path d="M22 4.5a9 9 0 0 1 12 0M24.2 7a5.6 5.6 0 0 1 7.6 0" stroke="#111" stroke-width="2" fill="none" stroke-linecap="round"/>
      <circle cx="28" cy="10" r="1.6" fill="#111"/>
      <rect x="38" y="2.5" width="19" height="8" rx="2.5" fill="#111"/>
    </symbol>
    <symbol id="phone" viewBox="0 0 20 20"><path d="M5 2.5l3 3.5-1.6 2a10 10 0 0 0 5.6 5.6l2-1.6 3.5 3-1.8 2.3C9 17 3 11 2.7 4.3z" fill="none" stroke="currentColor" stroke-width="1.1" stroke-linejoin="round"/></symbol>
    <symbol id="tab-msg" viewBox="0 0 26 24"><rect x="7" y="1" width="17" height="13" fill="none" stroke="currentColor"/><rect x="4" y="4" width="17" height="13" fill="#fff" stroke="currentColor"/><path d="M1 7h17v12H8l-4 3v-3H1z" fill="#fff" stroke="currentColor"/><path d="M4 11h11M4 14h9" stroke="currentColor"/></symbol>
    <symbol id="tab-family" viewBox="0 0 26 26"><g fill="none" stroke="currentColor"><circle cx="6" cy="4" r="2.5"/><circle cx="20" cy="4" r="2.5"/><circle cx="13" cy="11" r="2"/><path d="M3 8h6v8H8v9H4v-9H3zM17 8h6l1 9h-2v8h-4v-8h-2z M10.5 14h5v5h-1v6h-3v-6h-1z"/></g></symbol>
    <symbol id="tab-team" viewBox="0 0 30 24"><g fill="none" stroke="currentColor"><circle cx="7" cy="4" r="2.5"/><circle cx="23" cy="4" r="2.5"/><circle cx="15" cy="7" r="2.5"/><path d="M3 9h8v8M19 17V9h8v8H3M11 12h8v11h-8z"/></g></symbol>
    <symbol id="tab-time" viewBox="0 0 26 26"><circle cx="13" cy="13" r="11.5" fill="none" stroke="currentColor"/><path d="M13 13L8 6" stroke="currentColor"/><circle cx="13" cy="13" r="1" fill="currentColor"/></symbol>
    <symbol id="tab-setting" viewBox="0 0 26 26"><g fill="none" stroke="currentColor"><circle cx="13" cy="13" r="4"/><circle cx="13" cy="13" r="9"/><circle cx="13" cy="13" r="10.5" stroke-width="3" stroke-dasharray="3.4 3.2"/></g></symbol>
  </defs>
</svg>

<!-- Messages screen -->
<section class="screen screen--messages">
  <div class="status-bar"><span class="status-time">9:41</span><svg class="status-icons" width="58" height="12"><use href="#signal"/></svg></div>
  <header class="app-header">Messages</header>

  <div class="abs pending">Pending</div>

  <div class="task" style="top:186px">
    <svg class="task-icon" style="top:10px" width="18" height="24" viewBox="0 0 18 24"><path d="M9 1.5a6 6 0 0 0-6 6c0 4.5 6 11 6 11s6-6.5 6-11a6 6 0 0 0-6-6z" fill="none" stroke="#555"/><circle cx="9" cy="7.5" r="2" fill="none" stroke="#555"/><path d="M2 20.5h14" stroke="#555"/></svg>
    <div class="task-text">Check In @ Mara Quill<br>48 Elm Rd. Brookvale NH</div>
    <div class="task-date" style="top:32px">4-1-2019</div>
  </div>
  <div class="task-rule" style="left:34px;top:244px"></div>

  <div class="task" style="top:257px">
    <svg class="task-icon" style="top:12px" width="16" height="22" viewBox="0 0 16 22"><path d="M1 1h9l5 5v15H1z M10 1v5h5 M4 10h8M4 13h8M4 16h8" fill="none" stroke="#555"/></svg>
    <div class="task-text">Review Shift Note<br>Dana Whitlow</div>
    <div class="task-date" style="top:32px">10-1-2019</div>
  </div>
  <div class="task-rule" style="left:34px;top:320px"></div>

  <div class="task" style="top:338px">
    <svg class="task-icon" style="top:3px;color:#555" width="20" height="20"><use href="#phone"/></svg>
    <div class="task-text">Call Tom Hale</div>
    <div class="task-date" style="top:7px">12-1-2019</div>
  </div>

  <div class="abs notification">New Notification</div>

  <div class="tool" style="left:17px">
    <svg width="28" height="26" viewBox="0 0 28 26"><g stroke="#333" fill="none"><path d="M5 1v24M14 1v24M23 1v24"/><circle cx="5" cy="16" r="2.5" fill="#fff"/><circle cx="14" cy="8" r="2.5" fill="#fff"/><circle cx="23" cy="17" r="2.5" fill="#fff"/></g></svg>Filter List</div>
  <div class="tool" style="left:140px">
    <svg width="28" height="26" viewBox="0 0 28 26"><path d="M27 1L1 12l12 2 2 12z" fill="none" stroke="#333" stroke-linejoin="round"/></svg>Navigation</div>
  <div class="tool" style="left:259px">
    <svg width="28" height="26" viewBox="0 0 28 26"><rect x="5.5" y="4.5" width="17" height="17" fill="none" stroke="#333"/><path d="M14 8v10M9 13h10" stroke="#333"/></svg>Add New</div>

  <nav class="tab-bar">
    <div class="tab tab--active" style="left:11px"><svg width="26" height="24"><use href="#tab-msg"/></svg>Message</div>
    <div class="tab" style="left:101px"><svg width="26" height="26"><use href="#tab-family"/></svg>Family</div>
    <div class="tab" style="left:172px"><svg width="30" height="24"><use href="#tab-team"/></svg>Team</div>
    <div class="tab" style="left:250px"><svg width="26" height="26"><use href="#tab-time"/></svg>Time</div>
    <div class="tab" style="left:320px"><svg width="26" height="26"><use href="#tab-setting"/></svg>Setting</div>
  </nav>
</section>

<!-- Team Carer screen -->
<section class="screen screen--team">
  <div class="status-bar"><span class="status-time">9:41</span><svg class="status-icons" width="58" height="12"><use href="#signal"/></svg></div>
  <header class="app-header">Team Carer</header>

  <div class="abs sort-label">Sort By:</div>
  <div class="abs sort-select"><svg width="18" height="11" viewBox="0 0 18 11"><path d="M1 1l8 8 8-8" fill="none" stroke="var(--brand)" stroke-width="1.6"/></svg></div>

  <div class="carer-card" style="top:188px">
    <div class="avatar" role="img" aria-label="Portrait photo of team leader" style="background:radial-gradient(circle at 50% 45%,#c9a58f 0 30%,#3a2a26 60%)"></div>
    <div class="carer-name">Noa Feld</div>
    <div class="carer-role">Team Leader</div>
    <div class="carer-phone"><svg width="18" height="18" style="color:var(--brand-soft)"><use href="#phone"/></svg>+555 201 384</div>
  </div>

  <div class="carer-card" style="top:307px">
    <div class="avatar" role="img" aria-label="Portrait photo of alternate caregiver" style="background:radial-gradient(circle at 50% 50%,#e3c3a6 0 32%,#c59a5c 65%)"></div>
    <div class="carer-name">Ivy Marsh</div>
    <div class="carer-role">Alternate Caregiver</div>
    <div class="carer-phone"><svg width="18" height="18" style="color:var(--brand-soft)"><use href="#phone"/></svg>+555 201 384</div>
  </div>

  <div class="abs divider"></div>

  <div class="stat-label" style="left:17px;top:469px">Team Rating</div>
  <svg class="stars" style="top:470px" width="76" height="13" viewBox="0 0 76 13">
    <use href="#star" x="0" width="12" height="12" fill="var(--star)"/><use href="#star" x="15" width="12" height="12" fill="var(--star)"/>
    <use href="#star" x="30" width="12" height="12" fill="var(--star)"/><use href="#star" x="45" width="12" height="12" fill="var(--star)"/>
    <use href="#star" x="60" width="12" height="12" fill="none" stroke="var(--star-off)" stroke-width=".8"/>
  </svg>
  <div class="stat-label" style="left:17px;top:502px">Your Rating</div>
  <svg class="stars" style="top:503px" width="76" height="13" viewBox="0 0 76 13">
    <use href="#star" x="0" width="12" height="12" fill="var(--star)"/><use href="#star" x="15" width="12" height="12" fill="var(--star)"/>
    <use href="#star" x="30" width="12" height="12" fill="var(--star)"/><use href="#star" x="45" width="12" height="12" fill="var(--star)"/>
    <use href="#star" x="60" width="12" height="12" fill="none" stroke="var(--star-off)" stroke-width=".8"/>
  </svg>

  <div class="stat-label" style="left:205px;top:468px">Balance Scor</div>
  <div class="stat-value" style="top:464px">3.25</div>
  <div class="stat-label" style="left:205px;top:497px">Balance Amount</div>
  <div class="stat-value" style="top:493px">$98.75</div>
  <div class="stat-label" style="left:205px;top:524px">Total Earning Year</div>
  <div class="stat-value" style="top:520px;font-size:14px">$9,708.75</div>

  <svg class="abs chart" width="400" height="720" viewBox="0 0 400 720">
    <path d="M50 563V692H358" fill="none" stroke="#444" stroke-width="1.3"/>
    <g class="axis-label" text-anchor="end">
      <text x="42" y="620">3K</text><text x="42" y="645">2K</text><text x="42" y="670">1K</text><text x="38" y="696">0</text>
    </g>
    <g class="axis-label" text-anchor="middle">
      <text x="86" y="712">J</text><text x="157" y="712">K</text><text x="232" y="712">M</text><text x="308" y="712">N</text>
    </g>
    <polyline points="50,653 79,615 108,633 134,616 162,692 191,611 218,655 247,626 275,638 302,616 331,626 359,604"
      fill="none" stroke="var(--brand-soft)" stroke-width="1.4" stroke-linejoin="round"/>
  </svg>

  <nav class="tab-bar">
    <div class="tab tab--active" style="left:11px"><svg width="26" height="24"><use href="#tab-msg"/></svg>Message</div>
    <div class="tab" style="left:100px"><svg width="26" height="26"><use href="#tab-family"/></svg>Family</div>
    <div class="tab" style="left:172px"><svg width="30" height="24"><use href="#tab-team"/></svg>Team</div>
    <div class="tab" style="left:249px"><svg width="26" height="26"><use href="#tab-time"/></svg>Time</div>
    <div class="tab" style="left:319px"><svg width="26" height="26"><use href="#tab-setting"/></svg>Setting</div>
  </nav>
</section>
</body>
</html>
```